Salt Under Canvas: Years of Quiet Marching

I am an independent author writing a book about my life in the military while serving under the Don't Ask, Don't Tell Policy. The book will be published in both print and E-book format. For the print book, the front cover should be military dog tags with the main title printed on the tags while the subtitle printed at the top. The bottom portion of the front cover should have my name, "Bernard L. Whitfield". For the spine, the main title and my name should appear. The back will be reserved for the book's teaser as well as web contact information, both of which I will provide at a later time (still in development). The E-book cover can simply be the same as the front cover design for the print book.
Updates

Update! Change of heart on the positioning of the main title and the subtitle. Prefer the main title above the subtitle.

Thanks for all the submissions thus far.  Lots to choose from!  I finally have some info for the back covers.  If you have time, could you include the following on the back.

An unapologetic, first-hand account of life under Don’t Ask, Don’t Tell (make sure this is in big bold print at top)

(This is the teaser to be placed under) From 1993 to 2011, the Don’t Ask, Don’t Tell Policy affected the way LGBT military personnel not only interacted with people in public, but among each other in private.  From using code words in public to engaging in a secret sex life in private, the policy created a ridiculous social construct under which LGBT military personnel were expected to adhere.  For six and a half years, the author lived under these rules with the help of love-interests, friends, and allied co-workers.  Salt Under Canvas recalls episodes of the author living life to the fullest while covering his tracks just enough to avoid getting caught.  Despite enduring injustice, the author demonstrates just how resilient the LGBT community actually was.  Whether it was secret gatherings, a disciplined code of silence, or simply looking out for each other, Salt Under Canvas seeks to tell the story few have a guts to admit: how LGBT personnel got around the rules of Don’t Ask, Don’t Tell in order to maintain some sense of dignity

(The following contact info is to be placed toward the bottom centered.  Leave enough space to still place an ISBN)

www.facebook.com/saltcanvasbook           www.salt-canvas.com              www.twitter.com/saltcanvasbook

Hi Designers!

Lots of wonderful submissions that I appreciate very much.  Just an FYI, I intend to publish the print book cover via Print Harbor.  The instructions for book covers is found via the following link:

The design that I go with will need to adhere to these specifications.  No worries if your does not comply with these parameters at the time being.  I have every intention of offering payment for additional revisions to the covers.  Please send me quotes for additional revisions once the contest is over.  Also, to the design I pick, I will also require an E-book avatar, but we can discuss this later.

Target Market(s)

Target audience for this book are LGBT 25 and older, and women 25 and older

Requirements
Must have
• Dog Tags with main title printed on it.
Nice to have
• Print book and the E-book are going to have the same design, so try to ensure that the front cover design can catch attention as a thumbnail on a webpage.

```html
<!DOCTYPE html>
<html lang="en">
<head>
<meta charset="utf-8">
<title>Salt Under Canvas – Book Cover Spread</title>
<link href="https://fonts.googleapis.com/css2?family=Alfa+Slab+One&family=Open+Sans:wght@700;800&display=swap" rel="stylesheet">
<style>
  :root {
    --backdrop: #e4e4e4;
    --paper-light: #fdfdfd;
    --paper-shade: #dcdcdc;
    --ink: #111111;
    --ink-soft: #2a2a2a;
    --tag-metal-light: #e9e9e6;
    --tag-metal-dark: #8a8a86;
    --plate: #0d0d0d;
    --plate-text: #ffffff;
  }
  * { box-sizing: border-box; margin: 0; padding: 0; }
  html, body {
    width: 1200px; height: 800px; overflow: hidden;
    background: var(--backdrop);
  }
  .spread {
    position: absolute; left: 140px; top: 70px;
    width: 920px; height: 660px;
    display: flex;
    box-shadow: 0 8px 24px rgba(0,0,0,.18);
  }
  .cover {
    position: relative; width: 430px; height: 660px;
    overflow: hidden;
    background: linear-gradient(160deg, var(--paper-light) 0%, #eeeeee 60%, var(--paper-shade) 100%);
    color: var(--ink);
  }
  .spine {
    position: relative; width: 60px; height: 660px;
    background: linear-gradient(90deg, #d8d8d8, #f6f6f6 40%, #e2e2e2);
    display: flex; flex-direction: column; align-items: center; justify-content: space-between;
    padding: 26px 0 30px;
  }
  .spine-title, .spine-author {
    writing-mode: vertical-rl;
    white-space: nowrap;
  }
  .spine-title {
    font-family: "Alfa Slab One", serif;
    font-size: 30px; letter-spacing: 1px; color: var(--ink);
  }
  .spine-author {
    font-family: "Alfa Slab One", serif;
    font-size: 12px; letter-spacing: .5px;
  }

  /* Back cover */
  .back-author {
    position: absolute; top: 34px; right: 40px;
    font-family: "Alfa Slab One", serif; font-size: 10px; letter-spacing: .3px;
  }
  .back-title {
    position: absolute; top: 56px; left: 36px; right: 36px;
    font-family: "Alfa Slab One", serif; font-weight: 400;
    font-size: 29px; line-height: 1; letter-spacing: 0;
    color: var(--paper-light);
    -webkit-text-stroke: 1.5px var(--ink);
    text-shadow: 2px 2px 0 var(--ink);
    white-space: nowrap; text-align: left;
  }
  .back-rule {
    position: absolute; top: 100px; left: 36px; right: 36px;
    border-top: 3px solid var(--ink);
  }
  .back-subtitle {
    position: absolute; top: 110px; left: 36px; right: 36px;
    font-family: "Alfa Slab One", serif; font-size: 14px;
    letter-spacing: .6px; text-transform: uppercase; white-space: nowrap;
  }
  .back-teaser {
    position: absolute; top: 148px; left: 36px; right: 36px;
    font-family: "Open Sans", sans-serif; font-weight: 800;
    font-size: 11.6px; line-height: 1.32; text-transform: uppercase;
    text-align: justify; color: var(--ink-soft);
  }
  .plate {
    position: absolute; bottom: 40px; height: 64px;
    background: var(--plate); color: var(--plate-text);
    font-family: "Alfa Slab One", serif; font-size: 20px;
    display: flex; align-items: center; justify-content: center;
  }
  .plate-logo { left: 40px; width: 150px; }
  .plate-isbn { right: 40px; width: 150px; }

  /* Front cover */
  .tags-art {
    position: absolute; top: 30px; left: 24px; width: 380px; height: 360px;
    border-radius: 26px;
    background: linear-gradient(150deg, var(--tag-metal-light) 0%, #c6c6c2 55%, var(--tag-metal-dark) 100%);
  }
  .tag-text {
    position: absolute; text-align: center;
    font-family: "Alfa Slab One", serif; font-weight: 400; text-transform: uppercase;
    color: var(--ink);
  }
  .tag-title {
    top: 70px; left: 110px; width: 260px;
    font-size: 24px; line-height: 1.1; letter-spacing: 1px;
  }
  .tag-subtitle {
    top: 245px; left: 110px; width: 270px;
    font-size: 15px; line-height: 1.25; letter-spacing: .5px;
  }
  .front-author {
    position: absolute; bottom: 112px; right: 52px;
    font-family: "Alfa Slab One", serif; font-size: 14px; letter-spacing: .5px;
  }
</style>
</head>
<body>
  <main class="spread">
    <section class="cover back-cover">
      <p class="back-author">BERNARD L. WHITFIELD</p>
      <h2 class="back-title">SALT UNDER CANVAS</h2>
      <div class="back-rule"></div>
      <p class="back-subtitle">Years of Quiet Marching</p>
      <p class="back-teaser">
        Lorem ipsum dolor sit amet, consectetur adipisicing elit, sed do eiusmod tempor incididunt ut labore et dolore magna aliqua. Ut enim ad minim veniam, quis nostrud exercitation.
        Lorem ipsum dolor sit amet, consectetur adipisicing elit, sed do eiusmod tempor incididunt ut labore et dolore magna aliqua. Ut enim ad minim veniam, quis nostrud exercitation.
        Lorem ipsum dolor sit amet, consectetur adipisicing elit, sed do eiusmod tempor incididunt ut labore et dolore magna aliqua. Ut enim ad minim veniam, quis nostrud exercitation.
        Lorem ipsum dolor sit amet, consectetur adipisicing elit, sed do eiusmod tempor incididunt ut labore et dolore magna aliqua. Ut enim ad minim veniam, quis nostrud exercitation.
        Lorem ipsum dolor sit amet, consectetur adipisicing elit, sed do eiusmod tempor incididunt ut labore et dolore magna aliqua. Ut enim ad minim veniam, quis nostrud exercitation.
        Lorem ipsum dolor sit amet, consectetur adipisicing elit, sed do eiusmod tempor incididunt ut labore et dolore magna aliqua. Ut enim ad minim veniam.
      </p>
      <div class="plate plate-logo">LOGO</div>
      <div class="plate plate-isbn">ISBN</div>
    </section>

    <section class="spine">
      <span class="spine-title">SALT UNDER CANVAS</span>
      <span class="spine-author">BERNARD L. WHITFIELD</span>
    </section>

    <section class="cover front-cover">
      <div class="tags-art" role="img" aria-label="Two metal military dog tags on a beaded chain carrying the book title and subtitle"></div>
      <h1 class="tag-text tag-title">Salt Under<br>Canvas</h1>
      <p class="tag-text tag-subtitle">Years of<br>Quiet<br>Marching</p>
      <p class="front-author">BERNARD L. WHITFIELD</p>
    </section>
  </main>
</body>
</html>
```